Rising with Quiet Steps Book Cover

I need an eBook cover for my book
Title: Rising with Quiet Steps - Calm Your Habits, Shape Your Days
Subtitle: Leave Behind Restless Cycles and Welcome a Steady Path of Vigor and Contentment
Author: Marcus Pellington

This book is about learning the mechanisms behind weight loss and how to cultivate two qualities: discipline and consistency

Target Market(s)

Weight Loss, Mind Hack

Requirements
Nice to have
• I would like to see 2 images of the same woman standing back to back. The one on the left is overweight and sad and the one on the right is not overweight and smiling.

```html
<!DOCTYPE html>
<html lang="en">
<head>
<meta charset="utf-8">
<title>Rising with Quiet Steps — Book Cover</title>
<link rel="stylesheet" href="https://fonts.googleapis.com/css2?family=Oswald:wght@500;600&family=Roboto+Condensed:ital,wght@1,500&family=Montserrat:wght@800&display=swap">
<style>
  :root {
    --navy: #13175a;
    --navy-deep: #0e1148;
    --gold-light: #ffe14a;
    --gold: #f2b624;
    --gold-dark: #d99a1c;
    --white: #ffffff;
    --backdrop: #e9e8e9;
    --rule: #c9cad8;
  }
  * { margin: 0; padding: 0; box-sizing: border-box; }
  html, body { width: 1200px; height: 821px; overflow: hidden; background: var(--backdrop); }
  .stage { position: relative; width: 1200px; height: 821px; }
  .cover {
    position: absolute; left: 326px; top: 0;
    width: 548px; height: 821px; background: var(--white); overflow: hidden;
  }
  .cover-photo {
    position: absolute; left: 0; top: 0; width: 548px; height: 272px;
    background:
      radial-gradient(ellipse 28% 70% at 22% 40%, #d9a583 0%, rgba(217,165,131,0) 70%),
      radial-gradient(ellipse 30% 75% at 70% 38%, #c98a63 0%, rgba(201,138,99,0) 72%),
      linear-gradient(180deg, #fbf8f4 0%, #f3e6da 100%);
  }
  .title-band { position: absolute; left: 0; top: 250px; width: 548px; height: 360px; }
  .title-main, .title-small, .title-second, .tagline {
    position: absolute; left: 0; width: 100%; text-align: center;
    font-family: "Oswald", sans-serif; text-transform: uppercase; line-height: 1;
  }
  .gold-text {
    background: linear-gradient(90deg, var(--gold-light) 0%, var(--gold) 55%, var(--gold-dark) 100%);
    -webkit-background-clip: text; background-clip: text; color: transparent;
  }
  .title-main { top: 272px; font-size: 142px; font-weight: 600; letter-spacing: 2px; }
  .title-small {
    top: 405px; display: flex; align-items: center; justify-content: center; gap: 14px;
    font-size: 30px; font-weight: 600; color: var(--white);
  }
  .title-small::before, .title-small::after {
    content: ""; width: 175px; height: 3px; background: var(--white);
  }
  .title-small::before { background: linear-gradient(90deg, rgba(255,255,255,0), var(--white)); }
  .title-small::after { background: linear-gradient(90deg, var(--white), rgba(255,255,255,0)); }
  .title-second { top: 440px; font-size: 96px; font-weight: 600; color: var(--white); }
  .tagline { top: 548px; font-size: 33px; font-weight: 500; }
  .subtitle {
    position: absolute; left: 45px; width: 458px; top: 637px; padding: 8px 0;
    border-top: 1px solid var(--rule); border-bottom: 1px solid var(--rule);
    text-align: center; font-family: "Roboto Condensed", sans-serif; font-style: italic;
    font-weight: 500; font-size: 22.5px; line-height: 1.25; color: var(--navy);
  }
  .author-band {
    position: absolute; left: 0; top: 742px; width: 548px; height: 79px;
    border-top: 3px solid var(--navy);
    background: linear-gradient(90deg, var(--gold-dark) 0%, var(--gold-light) 40%, var(--gold) 75%, var(--gold-dark) 100%);
    display: flex; align-items: center; justify-content: center;
  }
  .author-name {
    font-family: "Montserrat", sans-serif; font-weight: 800; font-size: 40px;
    letter-spacing: 1px; text-transform: uppercase; color: var(--navy);
  }
</style>
</head>
<body>
<main class="stage">
  <article class="cover">
    <div class="cover-photo" role="img" aria-label="Photo of a fit woman and man in sportswear measuring their waists with tape measures"></div>

    <svg class="title-band" viewBox="0 0 548 360" aria-hidden="true">
      <defs>
        <linearGradient id="bandShade" x1="0" y1="0" x2="0" y2="1">
          <stop offset="0" stop-color="#13175a"/>
          <stop offset="1" stop-color="#0e1148"/>
        </linearGradient>
      </defs>
      <polygon fill="url(#bandShade)" points="
        0,14 18,10 30,16 52,9 70,13 88,6 110,12 128,8 146,15 170,9 190,12 212,5 236,11 258,7 280,14 300,8 322,12 344,4 366,10 388,7 410,13 432,6 452,11 476,8 498,14 520,7 538,11 548,8
        548,342 530,346 512,340 494,348 470,342 450,350 428,343 406,349 384,341 362,347 340,340 318,352 296,345 274,350 252,342 230,348 208,341 186,351 164,344 142,349 120,342 98,350 76,343 54,348 32,341 14,349 0,344"/>
    </svg>

    <h1 class="title-main gold-text">Rising</h1>
    <div class="title-small">With</div>
    <div class="title-second">Quiet Steps</div>
    <p class="tagline gold-text">Calm Your Habits, Shape Your Days</p>

    <p class="subtitle">Leave Behind Restless Cycles and Welcome<br>a Steady Path of Vigor and Contentment</p>

    <footer class="author-band">
      <span class="author-name">Marcus Pellington</span>
    </footer>
  </article>
</main>
</body>
</html>
```